Eastfield Commercial Card

I would like a modern, eye catching card based off my logo design.
Info to include:
Anders Voll (Card Name)
eastfieldcommercial.example (Website)
555 203 8841 (Office/fax)
555 287 3096 (Business Cell)
anders@eastfieldcommercial.example (Work email)

Target Market(s)

Commercial real estate brokers, property owners.

Colors
ec1f27
757575

Requirements
Must have
• Name and info above. Not be lame!:)

```html
<!DOCTYPE html>
<html lang="en">
<head>
<meta charset="utf-8">
<title>Eastfield Commercial Business Card</title>
<link href="https://fonts.googleapis.com/css2?family=Montserrat:wght@500;700&family=Roboto+Condensed:wght@400;500&display=swap" rel="stylesheet">
<style>
  :root {
    --brand-red: #ec1f27;
    --card-red: #a8191f;
    --brand-gray: #757575;
    --text-dark: #4a4a4a;
    --paper: #ffffff;
    --backdrop: #ebe7e1;
  }
  html, body {
    margin: 0;
    width: 1200px;
    height: 886px;
    overflow: hidden;
    background: var(--backdrop);
  }
  .stage {
    position: relative;
    width: 1200px;
    height: 886px;
  }
  .card {
    position: absolute;
    top: 288px;
    width: 540px;
    height: 310px;
    box-sizing: border-box;
    box-shadow: 0 6px 18px rgba(0,0,0,0.18);
  }
  .card-front { left: 40px; background: var(--paper); }
  .card-back  { left: 620px; background: var(--card-red); }

  .brand-lockup {
    position: absolute;
    left: 34px;
    top: 44px;
  }
  .brand-name {
    display: flex;
    align-items: center;
    gap: 10px;
    font-family: "Montserrat", sans-serif;
    font-weight: 700;
    font-size: 30px;
    letter-spacing: 0.5px;
    color: var(--brand-red);
    text-transform: uppercase;
    line-height: 1;
  }
  .brand-square {
    width: 26px;
    height: 26px;
    background: var(--brand-gray);
    flex: none;
  }
  .brand-tagline {
    display: flex;
    align-items: center;
    gap: 10px;
    margin: 8px 0 0 36px;
    font-family: "Montserrat", sans-serif;
    font-weight: 500;
    font-size: 13px;
    letter-spacing: 3.2px;
    color: var(--text-dark);
    text-transform: uppercase;
  }
  .brand-tagline .rule {
    display: block;
    height: 2px;
    width: 40px;
    background: var(--brand-gray);
  }

  .address {
    position: absolute;
    right: 34px;
    top: 150px;
    text-align: right;
    font-family: "Roboto Condensed", sans-serif;
    font-size: 14px;
    line-height: 1.4;
    color: var(--text-dark);
  }

  .contact {
    position: absolute;
    left: 34px;
    bottom: 30px;
    font-family: "Roboto Condensed", sans-serif;
  }
  .contact-name {
    font-size: 20px;
    font-weight: 500;
    color: var(--brand-red);
    text-transform: uppercase;
    margin-bottom: 8px;
  }
  .contact-list {
    list-style: none;
    margin: 0;
    padding: 0 0 0 12px;
    font-size: 13.5px;
    line-height: 1.45;
    color: var(--text-dark);
  }
  .contact-list li {
    display: flex;
    align-items: center;
    gap: 7px;
  }
  .contact-list svg {
    width: 11px;
    height: 11px;
    flex: none;
  }

  .back-mark {
    position: absolute;
    left: 34px;
    bottom: 36px;
    display: flex;
    align-items: center;
    gap: 10px;
    font-family: "Montserrat", sans-serif;
    font-weight: 700;
    font-size: 22px;
    color: var(--paper);
    text-transform: uppercase;
  }
  .back-mark .brand-square { background: var(--paper); width: 20px; height: 20px; }
</style>
</head>
<body>
<main class="stage">
  <section class="card card-front" aria-label="Card front">
    <div class="brand-lockup">
      <div class="brand-name"><span class="brand-square"></span>Eastfield Commercial</div>
      <div class="brand-tagline"><span class="rule"></span>Construction &amp; Roofing<span class="rule"></span></div>
    </div>

    <address class="address">48 Birchwood lane<br>Lakeview MN 55000</address>

    <div class="contact">
      <div class="contact-name">Anders Voll</div>
      <ul class="contact-list">
        <li>
          <svg viewBox="0 0 12 12" aria-hidden="true"><path d="M2.5 1 L4.5 1 L5.2 3.6 L4 4.6 Q5 7 7.4 8 L8.4 6.8 L11 7.5 L11 9.5 Q10.5 11 9 11 Q1 10 1 2.8 Q1 1.3 2.5 1Z" fill="var(--brand-red)"/></svg>
          555 203 8841
        </li>
        <li>
          <svg viewBox="0 0 12 12" aria-hidden="true"><rect x="3" y="0.8" width="6" height="10.4" rx="1" fill="none" stroke="var(--text-dark)" stroke-width="1.2"/><circle cx="6" cy="9.3" r="0.7" fill="var(--text-dark)"/></svg>
          555 287 3096
        </li>
        <li>
          <svg viewBox="0 0 12 12" aria-hidden="true"><rect x="0.5" y="2" width="11" height="8" fill="var(--brand-red)"/><path d="M0.5 2 L6 6.5 L11.5 2" fill="none" stroke="#fff" stroke-width="1"/></svg>
          anders@eastfieldcommercial.example
        </li>
        <li>
          <svg viewBox="0 0 12 12" aria-hidden="true"><circle cx="6" cy="6" r="5.5" fill="var(--brand-red)"/><circle cx="6" cy="6" r="2.5" fill="none" stroke="#fff" stroke-width="1"/><path d="M1 6 H11" stroke="#fff" stroke-width="0.8"/></svg>
          www.eastfieldcommercial.example
        </li>
      </ul>
    </div>
  </section>

  <section class="card card-back" aria-label="Card back">
    <div class="back-mark"><span class="brand-square"></span>Eastfield Commercial</div>
  </section>
</main>
</body>
</html>
```